Business card - mobile service

O KiraTel is a mobile family safety service based on tablets and smartphones.
The business card must have:
BASIC INFO
Company Logo
Name
Position / Job Title: Co-founder
Mobile Phone Number: +55 (11) 5080 6172
Land Line: +55 (11) 9087 614352
Email Address: name@kiratel-example.com
Web Site URL: www.kiratel-example.com
PROMOTIONAL INFO
Try KiraTel free Today!
Your personal promo code: xxxx-2222-uuuu-7777-1234
Promo code text explanation with the instructions about the trial offer
Updates
Dears,
One more must have: the KiraTel slogan:
Industry/Entity Type
Safety
Look and feel
Each slider illustrates characteristics of the customer's brand and the style your logo design should communicate.

```html
<!DOCTYPE html>
<html lang="en">
<head>
<meta charset="utf-8">
<title>KiraTel Business Card</title>
<link rel="stylesheet" href="https://fonts.googleapis.com/css2?family=Open+Sans:wght@400;600;700&display=swap">
<style>
  :root {
    --stage: #6f1819;
    --card-white: #ffffff;
    --brand-blue: #38a7df;
    --brand-yellow: #f5c30f;
    --text-blue: #2f9fd9;
    --ink-white: #ffffff;
    --ink-soft: rgba(255, 255, 255, 0.85);
    --code-panel: rgba(255, 255, 255, 0.16);
    --shadow: rgba(0, 0, 0, 0.35);
  }
  * { margin: 0; padding: 0; box-sizing: border-box; }
  html, body {
    width: 1200px;
    height: 900px;
    overflow: hidden;
    background: var(--stage);
    font-family: "Open Sans", Arial, sans-serif;
  }
  .canvas { position: relative; width: 1200px; height: 900px; }

  .card {
    position: absolute;
    border-radius: 24px;
    overflow: hidden;
    box-shadow: 0 6px 18px var(--shadow);
  }

  /* Front */
  .card-front {
    left: 326px; top: 34px;
    width: 610px; height: 392px;
    background: var(--card-white);
  }
  .front-accent {
    position: absolute;
    right: 0; top: 22px; bottom: 0;
    width: 20px;
    background: var(--brand-yellow);
    border-top-left-radius: 14px;
  }
  .brand-name {
    position: absolute;
    left: 44px; top: 150px;
    font-weight: 700;
    font-size: 62px;
    line-height: 1;
    letter-spacing: -1px;
    color: var(--brand-blue);
  }
  .identity {
    position: absolute;
    right: 54px; top: 110px;
    text-align: right;
  }
  .identity .person-name {
    font-weight: 700;
    font-size: 25px;
    line-height: 1.1;
    color: var(--text-blue);
  }
  .identity .person-role {
    font-weight: 400;
    font-size: 19px;
    line-height: 1.2;
    color: var(--brand-yellow);
  }
  .contact-list {
    position: absolute;
    right: 54px; top: 220px;
    list-style: none;
  }
  .contact-list li {
    display: flex;
    justify-content: flex-end;
    align-items: center;
    gap: 10px;
    height: 25px;
    font-size: 16px;
    color: var(--text-blue);
  }
  .contact-list b { font-weight: 700; }
  .contact-list svg { width: 18px; height: 18px; flex: none; }

  /* Back */
  .card-back {
    left: 318px; top: 466px;
    width: 620px; height: 398px;
    background: var(--brand-blue);
    color: var(--ink-white);
  }
  .back-slogan {
    position: absolute;
    left: 26px; top: 40px;
    font-size: 18px;
    font-weight: 600;
    color: var(--ink-soft);
  }
  .back-url {
    position: absolute;
    left: 26px; top: 120px;
    font-size: 30px;
  }
  .back-url b { font-weight: 700; }
  .promo {
    position: absolute;
    left: 26px; right: 26px; top: 196px;
  }
  .promo-title {
    font-size: 22px;
    font-weight: 700;
    color: var(--brand-yellow);
  }
  .promo-code {
    display: inline-block;
    margin-top: 10px;
    padding: 6px 14px;
    border-radius: 8px;
    background: var(--code-panel);
    font-size: 16px;
  }
  .promo-code b { font-weight: 700; letter-spacing: 0.5px; }
  .promo-note {
    margin-top: 12px;
    font-size: 13px;
    line-height: 1.45;
    color: var(--ink-soft);
  }
</style>
</head>
<body>
<main class="canvas">

  <section class="card card-front" aria-label="Business card front">
    <div class="front-accent"></div>
    <div class="brand-name">KiraTel</div>

    <div class="identity">
      <div class="person-name">Your Name</div>
      <div class="person-role">Co-founder</div>
    </div>

    <ul class="contact-list">
      <li>+55 (11) 5080 6172
        <svg viewBox="0 0 18 18" aria-hidden="true"><rect x="5" y="1" width="8" height="16" rx="1.5" fill="var(--brand-yellow)"/><rect x="6.5" y="3" width="5" height="8" fill="#fff"/></svg>
      </li>
      <li>+55 (11) 9087 614352
        <svg viewBox="0 0 18 18" aria-hidden="true"><path d="M1 6 Q9 1 17 6 L15 8 L12 7 L12 5 Q9 4 6 5 L6 7 L3 8 Z" fill="var(--brand-yellow)"/><rect x="3" y="9" width="12" height="7" rx="1" fill="var(--brand-yellow)"/><circle cx="9" cy="12.5" r="2" fill="#fff"/></svg>
      </li>
      <li><span>name@<b>kiratel-example</b>.com</span>
        <svg viewBox="0 0 18 18" aria-hidden="true"><rect x="1" y="4" width="16" height="11" fill="var(--brand-yellow)"/><path d="M1 4 L9 10 L17 4" fill="none" stroke="#fff" stroke-width="1.4"/></svg>
      </li>
      <li><span>www.<b>kiratel-example</b>.com</span>
        <svg viewBox="0 0 18 18" aria-hidden="true"><rect x="3" y="3" width="12" height="9" fill="none" stroke="var(--brand-yellow)" stroke-width="1.8"/><rect x="1" y="13" width="16" height="2.5" fill="var(--brand-yellow)"/></svg>
      </li>
    </ul>
  </section>

  <section class="card card-back" aria-label="Business card back">
    <div class="back-slogan">Your family, always within reach.</div>
    <div class="back-url">www.<b>kiratel-example</b>.com</div>
    <div class="promo">
      <div class="promo-title">Try KiraTel free Today!</div>
      <div class="promo-code">Your personal promo code: <b>xxxx-2222-uuuu-7777-1234</b></div>
      <p class="promo-note">Install the app on your smartphone or tablet, create an account and enter the code above to start your free trial. The offer is valid for one family account.</p>
    </div>
  </section>

</main>
</body>
</html>
```